Consulting Company Business Card

I am looking for a minimalist, classy, professional design on my business card. I would like it to be double-sided. I want to use the font and color scheme of my logo which are attached. Please be creative in the designs that you send me. I want to play off the design of my logo with the inner C that is Green and Blue broken up with the white.
Target Market(s)
Small Businesses
Industry/Entity Type
Consulting
Contact Information for Business Card
Dale M. Whitcombe, CPA CGMA, 555-014-2873, dwhitcombe@vorantaadvisory.example, www.vorantaadvisory.example

```html
<!DOCTYPE html>
<html lang="en">
<head>
<meta charset="utf-8">
<title>Voranta Advisory — Business Card</title>
<link href="https://fonts.googleapis.com/css2?family=Montserrat:wght@500;600;700&family=Open+Sans:wght@400&display=swap" rel="stylesheet">
<style>
  :root {
    --page-bg: #e6e2dc;
    --navy-deep: #15182a;
    --navy-mid: #2c3046;
    --accent-green: #1f4a40;
    --edge-light: #d9d3c8;
    --frost-top: #f2efea;
    --frost-bottom: #d8d1c6;
    --ink-light: #e6e2da;
    --ink-muted: #cfc9bf;
    --brand-ink: #1a1d2c;
  }
  * { margin: 0; padding: 0; box-sizing: border-box; }
  html, body { width: 1200px; height: 969px; overflow: hidden; background: var(--page-bg); }
  .canvas { position: relative; width: 1200px; height: 969px; }
  .card {
    position: absolute; left: 80px; top: 188px;
    width: 1040px; height: 592px;
    border-radius: 28px; overflow: hidden;
    box-shadow: 0 10px 30px rgba(0,0,0,0.18);
  }
  .card-art { position: absolute; inset: 0; }
  .holder { position: absolute; left: 44px; top: 195px; color: var(--ink-light); }
  .holder-name { font-family: "Montserrat", sans-serif; font-weight: 600; font-size: 30px; letter-spacing: 0.2px; }
  .holder-title { font-family: "Montserrat", sans-serif; font-weight: 600; font-size: 19px; color: var(--ink-muted); margin-top: 4px; }
  .contact-list { list-style: none; margin-top: 40px; font-family: "Open Sans", sans-serif; font-size: 21px; color: var(--ink-muted); }
  .contact-item { display: flex; align-items: center; gap: 12px; height: 30px; }
  .contact-icon { width: 18px; height: 18px; flex: none; }
  .brand-name {
    position: absolute; left: 800px; top: 340px; transform: translateX(-50%);
    font-family: "Montserrat", sans-serif; font-weight: 700; font-size: 26px;
    color: var(--brand-ink); letter-spacing: 1.5px; white-space: nowrap;
  }
</style>
</head>
<body>
<div class="canvas">
  <div class="card">
    <svg class="card-art" viewBox="0 0 1040 592" width="1040" height="592" aria-hidden="true">
      <defs>
        <linearGradient id="frost" x1="0" y1="0" x2="0" y2="1">
          <stop offset="0" stop-color="#f2efea"/>
          <stop offset="1" stop-color="#d8d1c6"/>
        </linearGradient>
        <radialGradient id="panel" cx="0.3" cy="0.55" r="0.8">
          <stop offset="0" stop-color="#2f3349"/>
          <stop offset="1" stop-color="#15182a"/>
        </radialGradient>
      </defs>
      <rect class="frosted-area" width="1040" height="592" fill="url(#frost)"/>
      <path class="accent-band" d="M628,0 H672 C555,110 480,270 525,430 C548,510 590,560 612,592 H600 C560,540 505,470 490,400 C470,260 530,110 628,0Z" fill="var(--accent-green)"/>
      <path class="accent-line" d="M676,0 H682 C565,115 495,270 535,430 C555,505 600,560 630,592 H625 C590,555 545,500 528,430 C490,270 560,110 676,0Z" fill="var(--edge-light)"/>
      <path class="dark-panel" d="M0,0 H630 C530,110 465,260 490,400 C505,480 560,545 675,592 H0Z" fill="url(#panel)"/>
    </svg>

    <div class="holder">
      <div class="holder-name">Dale M. Whitcombe,</div>
      <div class="holder-title">CPA CGMA</div>
      <ul class="contact-list">
        <li class="contact-item">
          <svg class="contact-icon" viewBox="0 0 18 18"><rect x="4" y="1" width="10" height="16" rx="2" fill="none" stroke="currentColor" stroke-width="1.6"/><line x1="7.5" y1="14" x2="10.5" y2="14" stroke="currentColor" stroke-width="1.4"/></svg>
          <span>555-014-2873</span>
        </li>
        <li class="contact-item">
          <svg class="contact-icon" viewBox="0 0 18 18"><rect x="1" y="4" width="16" height="11" fill="none" stroke="currentColor" stroke-width="1.6"/><polyline points="1,4 9,10 17,4" fill="none" stroke="currentColor" stroke-width="1.6"/></svg>
          <span>dwhitcombe@vorantaadvisory.example</span>
        </li>
        <li class="contact-item">
          <svg class="contact-icon" viewBox="0 0 18 18"><circle cx="9" cy="9" r="7.5" fill="none" stroke="currentColor" stroke-width="1.6"/><ellipse cx="9" cy="9" rx="3.2" ry="7.5" fill="none" stroke="currentColor" stroke-width="1.2"/><line x1="1.5" y1="9" x2="16.5" y2="9" stroke="currentColor" stroke-width="1.2"/></svg>
          <span>www.vorantaadvisory.example</span>
        </li>
      </ul>
    </div>

    <div class="brand-name">VORANTA ADVISORY</div>
  </div>
</div>
</body>
</html>
```